Pet store web design

I would like to redesign my current online store (http://brindlecove.example)
I'm looking for a clean, modern design. Any ideas are welcome..

Industry/Entity Type

Pet

Number of Pages Required

3 page

```html
<!DOCTYPE html>
<html lang="en">
<head>
<meta charset="utf-8">
<title>Brindle Cove – Pet Store</title>
<link rel="stylesheet" href="https://fonts.googleapis.com/css2?family=Open+Sans:wght@400;600;700;800&display=swap">
<style>
:root{
  --yellow:#f6c21a;
  --red:#e8473c;
  --teal:#1f8e95;
  --teal-dark:#167479;
  --ink:#333;
  --muted:#888;
  --line:#e3e3e3;
  --bg:#f2f2f2;
  --hero-a:#f7f1e4;
  --hero-b:#ede3cd;
}
*{box-sizing:border-box;margin:0;padding:0}
html,body{width:717px;height:1200px;overflow:hidden}
body{font-family:"Open Sans",Arial,sans-serif;color:var(--ink);background:#fff;font-size:6px;position:relative}
.wrap{width:647px;margin:0 auto;position:relative}

/* header */
.topbar{height:38px}
.logo{position:absolute;left:0;top:6px;display:flex;align-items:center;gap:4px;font-weight:800;font-size:12px;color:var(--red)}
.logo i{width:12px;height:12px;border-radius:50%;background:var(--yellow);display:block}
.tagline{position:absolute;left:152px;top:9px;color:var(--red);font-weight:700;font-size:8.5px}
.account{position:absolute;right:0;top:5px;display:flex;gap:11px;font-size:4.8px;color:var(--muted);text-transform:uppercase}
.search{position:absolute;right:70px;top:20px;width:66px;height:10px;border:1px solid var(--line);font-size:4.5px;color:#aaa;padding:2px 3px}
.bag{position:absolute;right:0;top:21px;font-size:4.5px;color:var(--muted);display:flex;align-items:center;gap:3px}
.bag i{width:7px;height:7px;border:1px solid #999;display:block}

.nav{background:var(--yellow);height:22px}
.nav ul{list-style:none;display:flex;height:22px}
.nav li{width:46px;text-align:center;line-height:22px;font-size:5px;font-weight:700;color:#fff;text-transform:uppercase}
.nav li.active{background:var(--red)}
.social{position:absolute;right:0;top:5px;display:flex;gap:3px}
.social span{width:11px;height:11px;border-radius:50%;background:var(--red);display:block}
.social span:nth-child(2){background:#e15b4f}
.social span:nth-child(3){background:#3b7bc4}

.promo-bar{background:var(--teal);height:29px;margin-top:8px}
.promo-bar .wrap{display:flex;gap:24px;align-items:center;height:29px;color:#fff;font-size:8px;font-weight:600;text-transform:uppercase}
.promo-bar .item{display:flex;align-items:center;gap:5px}

/* hero */
.hero{height:351px;background:linear-gradient(180deg,var(--hero-a),var(--hero-b));position:relative}
.hero h1{position:absolute;left:60px;top:140px;color:var(--teal);font-size:22px;font-weight:800}
.hero p{position:absolute;left:60px;top:172px;width:215px;font-size:5.5px;line-height:8px;color:#555}
.btn-yellow{background:var(--yellow);color:#fff;font-weight:700;font-size:5px;text-transform:uppercase;display:inline-block;text-align:center}
.hero .btn-yellow{position:absolute;left:60px;top:207px;width:44px;height:13px;line-height:13px}
.hero-art{position:absolute;left:335px;top:20px;width:300px;height:240px;border-radius:20px;background:radial-gradient(ellipse at 50% 55%,#d9c7a5 0%,#b89c77 45%,rgba(237,227,205,0) 72%)}
.arrow{position:absolute;top:150px}
.arrow.l{left:8px}.arrow.r{right:8px}

.offers{position:absolute;left:35px;top:263px;display:flex;gap:13px}
.offer{width:204px;height:70px;background:#fff;box-shadow:0 1px 3px rgba(0,0,0,.15);position:relative}
.offer .badge{position:absolute;left:8px;top:8px;width:20px;height:20px;border-radius:50%;background:var(--red)}
.offer .pic{position:absolute;left:32px;top:6px;width:52px;height:58px;background:linear-gradient(135deg,#c44,#3a4a6a)}
.offer h3{position:absolute;left:92px;top:10px;font-size:7px;color:var(--red);font-weight:700}
.offer p{position:absolute;left:92px;top:21px;width:100px;font-size:4.5px;line-height:6px;color:#777}
.offer .btn-yellow{position:absolute;left:92px;top:48px;width:44px;height:10px;line-height:10px;font-size:4.5px}

/* popular */
.section-head{margin-top:35px;height:24px;background:var(--bg);display:flex;align-items:center;justify-content:space-between;padding:0 8px;font-weight:800;font-size:8px;text-transform:uppercase}
.section-head i{width:10px;height:10px;border-radius:50%;background:#ccc;display:block}
.products{display:flex;gap:12px;margin-top:13px}
.card{width:152px;height:242px;border:1px solid var(--line);text-align:center;position:relative}
.card .head{background:var(--yellow);height:14px;line-height:14px;font-size:5px;font-weight:700;color:#fff;text-align:left;padding-left:8px;text-transform:uppercase}
.card .pic{margin:18px auto 0;width:80px;height:80px;border-radius:6px}
.card h4{margin-top:26px;font-size:5px;font-weight:700;text-transform:uppercase}
.card .price{margin-top:6px;font-size:7px;color:var(--red);font-weight:700}
.card .stars{margin-top:6px;font-size:5px;color:var(--yellow)}
.card .stars em{color:var(--muted);font-style:normal}
.btn-red{background:var(--red);color:#fff;font-weight:700;font-size:5px;text-transform:uppercase;width:46px;height:13px;line-height:13px;margin:10px auto 0}

/* features */
.features{margin-top:45px;border-top:1px solid var(--line);border-bottom:1px solid var(--line);height:62px;display:flex;align-items:center;justify-content:space-around}
.feature{display:flex;gap:8px;align-items:flex-start;width:180px}
.feature h5{color:var(--teal);font-size:6.5px;font-weight:700;text-transform:uppercase}
.feature p{font-size:4.8px;line-height:6.5px;color:#777;margin-top:3px}

/* newsletter */
.newsletter{background:var(--bg);height:30px;margin-top:24px}
.newsletter .wrap{display:flex;align-items:center;height:30px;font-size:5.5px;font-weight:700;text-transform:uppercase}
.newsletter .field{margin-left:68px;width:90px;height:11px;background:#fff;border:1px solid var(--line);font-size:4.5px;color:#aaa;font-weight:400;padding:2px 3px;text-transform:none}
.newsletter .sub{background:var(--red);color:#fff;width:55px;height:11px;line-height:11px;text-align:center;font-size:4.5px}
.newsletter .social{top:9px}

/* footer */
.footer{display:flex;margin-top:28px;height:150px}
.footer .col{width:162px}
.footer h6{font-size:5.5px;font-weight:800;text-transform:uppercase;margin-bottom:6px}
.footer li{list-style:none;font-size:4.8px;color:#777;line-height:8px}
.pay{display:flex;gap:3px;margin-top:4px}
.pay span{width:16px;height:10px;border:1px solid var(--line);background:#f7f7f7;display:block}
.copyright{position:absolute;left:0;right:0;bottom:0;height:24px;background:var(--bg);text-align:center;line-height:24px;font-size:4.8px;color:#888;text-transform:uppercase}
</style>
</head>
<body>
<header class="topbar">
  <div class="wrap">
    <div class="logo"><i></i>Brindle Cove</div>
    <div class="tagline">30 New Pet Products Every Month</div>
    <nav class="account"><span>My Account</span><span>My Cart</span><span>Checkout</span><span>My Wishlist</span><span>Login</span></nav>
    <div class="search">Search</div>
    <div class="bag"><i></i>Your bag $0.00</div>
  </div>
</header>

<nav class="nav">
  <div class="wrap">
    <ul><li class="active">Home</li><li>Dog</li><li>Cat</li><li>Bird</li><li>Fish</li><li>Small Pet</li></ul>
    <div class="social"><span></span><span></span><span></span></div>
  </div>
</nav>

<div class="promo-bar">
  <div class="wrap">
    <div class="item">
      <svg width="10" height="10" viewBox="0 0 10 10"><path d="M1 5l3 3 5-6" stroke="#fff" stroke-width="1.5" fill="none"/></svg>
      Free delivery on orders over $79
    </div>
    <div class="item">
      <svg width="10" height="10" viewBox="0 0 10 10"><path d="M1 5l3 3 5-6" stroke="#fff" stroke-width="1.5" fill="none"/></svg>
      Shop the collections
    </div>
  </div>
</div>

<section class="hero">
  <svg class="arrow l" width="8" height="16" viewBox="0 0 8 16"><path d="M7 1L1 8l6 7" stroke="#999" fill="none"/></svg>
  <svg class="arrow r" width="8" height="16" viewBox="0 0 8 16"><path d="M1 1l6 7-6 7" stroke="#999" fill="none"/></svg>
  <h1>All Your Pet Needs..!</h1>
  <p>Accusamus et iusto odio dignissimos ducimus qui blanditiis praesentium voluptatum deleniti atque corrupti quos dolores et quas molestias excepturi sint occaecati cupiditate non provident...</p>
  <span class="btn-yellow">Add to cart</span>
  <div class="hero-art" role="img" aria-label="Group of pets: a large dog, a parrot, cats and puppies"></div>

  <div class="offers">
    <div class="offer"><span class="badge"></span><div class="pic" role="img" aria-label="Pet winter jacket"></div><h3>Fall / Winter</h3><p>Warm coats and cosy layers for cold days outside.</p><span class="btn-yellow">Shop now</span></div>
    <div class="offer"><span class="badge"></span><div class="pic" role="img" aria-label="Pet winter sweater"></div><h3>Fall / Winter</h3><p>Warm coats and cosy layers for cold days outside.</p><span class="btn-yellow">Shop now</span></div>
    <div class="offer"><span class="badge"></span><div class="pic" role="img" aria-label="Pet winter boots"></div><h3>Fall / Winter</h3><p>Warm coats and cosy layers for cold days outside.</p><span class="btn-yellow">Shop now</span></div>
  </div>
</section>

<div class="wrap">
  <div class="section-head">Most Popular <i></i></div>
  <div class="products">
    <div class="card"><div class="head">Shop for dogs ›</div><div class="pic" role="img" aria-label="Dog costume" style="background:linear-gradient(135deg,#cfd8e6,#7f9ab8)"></div><h4>Dog Sailor Costume - Large</h4><div class="price">$30.65</div><div class="stars">★★★★☆ <em>10 Reviews</em></div><div class="btn-red">Add to cart</div></div>
    <div class="card"><div class="head">Shop for dogs ›</div><div class="pic" role="img" aria-label="Christmas dog shirt" style="background:linear-gradient(135deg,#f1c4c4,#c9403a)"></div><h4>Christmas Tree Shirt Dog</h4><div class="price">$35.38</div><div class="stars">★★★★☆ <em>10 Reviews</em></div><div class="btn-red">Add to cart</div></div>
    <div class="card"><div class="head">Shop for dogs ›</div><div class="pic" role="img" aria-label="Round pet bed" style="background:linear-gradient(135deg,#e6e2c6,#b6b07a)"></div><h4>Nest Bed - Large Oat Suede</h4><div class="price">$290.31</div><div class="stars">★★★★☆ <em>10 Reviews</em></div><div class="btn-red">Add to cart</div></div>
    <div class="card"><div class="head">Shop for dogs ›</div><div class="pic" role="img" aria-label="Dog treadmill" style="background:linear-gradient(135deg,#d9d9d9,#c0392b)"></div><h4>Stridewell Dog Treadmill</h4><div class="price">$865.83</div><div class="stars">★★★★☆ <em>10 Reviews</em></div><div class="btn-red">Add to cart</div></div>
  </div>

  <div class="features">
    <div class="feature">
      <svg width="18" height="14" viewBox="0 0 18 14"><rect x="1" y="2" width="10" height="8" fill="none" stroke="#1f8e95" stroke-width="1.3"/><path d="M11 5h4l2 3v2h-6z" fill="none" stroke="#1f8e95" stroke-width="1.3"/><circle cx="4" cy="11.5" r="1.6" fill="#1f8e95"/><circle cx="14" cy="11.5" r="1.6" fill="#1f8e95"/></svg>
      <div><h5>Delivery</h5><p>Fast delivery on every order, tracked from our door to yours.</p></div>
    </div>
    <div class="feature">
      <svg width="16" height="16" viewBox="0 0 16 16"><path d="M13 8a5 5 0 1 1-2-4" fill="none" stroke="#1f8e95" stroke-width="1.4"/><path d="M9 2h3v3" fill="none" stroke="#1f8e95" stroke-width="1.4"/></svg>
      <div><h5>Returns</h5><p>Easy returns within thirty days, no questions asked.</p></div>
    </div>
    <div class="feature">
      <svg width="16" height="16" viewBox="0 0 16 16"><path d="M4 2l3 3-2 2c1 2 2 3 4 4l2-2 3 3-2 2C7 14 2 9 2 4z" fill="#1f8e95"/></svg>
      <div><h5>Let us help</h5><p>Our team is here to answer your questions every day.</p></div>
    </div>
  </div>
</div>

<div class="newsletter">
  <div class="wrap">
    Get our recent updates through your email id
    <span class="field">Enter your email id</span>
    <span class="sub">Subscribe now</span>
    <div class="social"><span></span><span></span><span></span></div>
  </div>
</div>

<div class="wrap">
  <div class="footer">
    <div class="col"><h6>Shop now</h6><ul><li>Dog</li><li>Cat</li><li>Fish</li><li>Bird</li><li>Aquarium</li><li>Small Animal</li></ul></div>
    <div class="col"><h6>Shopping online</h6><ul><li>Delivery Information</li><li>Privacy Policy</li><li>Returns Policy</li><li>Terms and Conditions</li><li>FAQ's</li></ul></div>
    <div class="col"><h6>About us</h6><ul><li>About Us</li><li>Careers</li><li>Pet Blog</li><li>Contact Us</li></ul><h6 style="margin-top:8px">Payment options</h6><div class="pay"><span></span><span></span><span></span></div></div>
    <div class="col"><h6>Services</h6><ul><li>Pet Grooming</li><li>Pet Adoption</li><li>Pet Training</li><li>Pet Hotel</li><li>Quality Service</li></ul></div>
  </div>
</div>

<div class="copyright">Copyright © 2015 Brindle Cove. All rights reserved</div>
</body>
</html>
```